Rest Bloom Soar: Mental Health Counseling brochure

I need a brochure that highlights my services. The inside panels should highlight: Individual therapy, Couples Therapy, Group Therapy and Psychotherapy in French. One other panels should include information on fees and insurance, and the second an "About me" panel. The final panel should be my contact ion.

You can pull all the text from my website and photos too. I am including files below that include shortened versions of the website text.

Business moto: Rest. Bloom Soar.
Your personal journey begins here.

Contact info is available on the web. A current address and a new address should be listed on the contact panel

Current location (until 12/23/2016): … 9address on website)
New Location (1/1/2017): 2424 Marbury Ave. NW, Suite 303
Washington DC 20016

Target Market(s)

professionals, adults, conservative. Men and women. Artsy photos. no stock photos.

Industry/Entity Type

Mental Health

Font styles to use
Sans Serif

Colors
33a6d7
33b8a4

Requirements
Must have
• no great gimmicks, something pretty, see my website. Text, photos or a photo from my website, my professional photo also from my website. www.MarissaTolvenLPC.example
• Calm, Artsy, elegant, young professionals, seasoned professionals.
Should not have
• no stock photos...

```html
<!DOCTYPE html>
<html lang="en">
<head>
<meta charset="utf-8">
<title>Rest Bloom Soar – Brochure Cover</title>
<link rel="stylesheet" href="https://fonts.googleapis.com/css2?family=Roboto+Condensed:wght@400;700&display=swap">
<style>
  :root {
    --backdrop: #b9b4b2;
    --paper: #f3f3f3;
    --paper-shade: #e6e6e6;
    --teal: #5cc8bb;
    --teal-deep: #33b8a4;
    --charcoal: #444546;
    --white: #ffffff;
    --photo-sky: #dfe7e4;
    --photo-rock: #5b6b64;
    --photo-water: #2f4a5c;
  }
  * { margin: 0; padding: 0; box-sizing: border-box; }
  html, body {
    width: 1200px;
    height: 857px;
    overflow: hidden;
    background: var(--backdrop);
  }
  .canvas {
    position: relative;
    width: 1200px;
    height: 857px;
  }
  .cover {
    position: absolute;
    left: 310px;
    top: 23px;
    width: 580px;
    height: 810px;
    background: linear-gradient(160deg, var(--paper), var(--paper-shade));
    overflow: hidden;
    font-family: "Roboto Condensed", "Arial Narrow", sans-serif;
    color: var(--charcoal);
  }
  .cover-art {
    position: absolute;
    inset: 0;
    width: 580px;
    height: 810px;
  }
  .practice-name {
    position: absolute;
    right: 34px;
    top: 58px;
    display: flex;
    align-items: center;
    gap: 10px;
    font-weight: 700;
    font-size: 26px;
    line-height: 1.05;
    color: var(--charcoal);
    text-align: right;
  }
  .practice-name .mark {
    width: 16px;
    height: 16px;
    border-radius: 50%;
    background: var(--teal-deep);
    flex: none;
  }
  .tagline-block {
    position: absolute;
    left: 52px;
    top: 532px;
    width: 300px;
  }
  .motto {
    font-weight: 700;
    font-size: 31px;
    letter-spacing: 0.2px;
    margin-left: 14px;
    line-height: 1;
  }
  .journey-line {
    position: relative;
    margin-top: 6px;
    height: 130px;
  }
  .journey-initial {
    position: absolute;
    left: 0;
    top: -8px;
    font-weight: 700;
    font-size: 140px;
    line-height: 1;
    color: var(--teal);
  }
  .journey-intro {
    position: absolute;
    left: 40px;
    top: 0;
    font-weight: 700;
    font-size: 31px;
    line-height: 1;
    padding-bottom: 4px;
    border-bottom: 3px solid var(--charcoal);
    white-space: nowrap;
  }
  .journey-word {
    position: absolute;
    left: 62px;
    top: 36px;
    font-weight: 700;
    font-size: 70px;
    line-height: 1;
    color: var(--teal);
    letter-spacing: 0.5px;
  }
  .begins-bar {
    display: inline-block;
    margin-left: 16px;
    margin-top: -6px;
    padding: 3px 48px 3px 8px;
    background: var(--charcoal);
    color: var(--white);
    font-weight: 700;
    font-size: 26px;
    line-height: 1.15;
  }
</style>
</head>
<body>
<main class="canvas">
  <section class="cover">
    <svg class="cover-art" viewBox="0 0 580 810" xmlns="http://www.w3.org/2000/svg">
      <defs>
        <linearGradient id="landscapeTones" x1="0" y1="0" x2="0.4" y2="1">
          <stop offset="0" stop-color="var(--photo-sky)"/>
          <stop offset="0.45" stop-color="var(--photo-rock)"/>
          <stop offset="1" stop-color="var(--photo-water)"/>
        </linearGradient>
      </defs>
      <path class="accent-band" d="M92,0 C110,330 320,520 580,548 L580,515 C340,480 160,300 140,0 Z" fill="var(--teal)"/>
      <path class="photo-area" role="img" aria-label="Photograph: a person standing on a mountain cliff ledge above a fjord lake" d="M140,0 C160,300 340,480 580,515 L580,0 Z" fill="url(#landscapeTones)"/>
      <path class="journey-arc" d="M0,292 C210,270 395,470 445,810 L402,810 C362,500 200,312 0,304 Z" fill="var(--charcoal)"/>
      <circle class="arc-mark" cx="150" cy="300" r="30" fill="var(--teal)"/>
    </svg>

    <div class="practice-name">
      <span class="mark"></span>
      <span>Marissa Tolven<br>LPC</span>
    </div>

    <div class="tagline-block">
      <p class="motto">Rest. Bloom. Soar.</p>
      <div class="journey-line">
        <span class="journey-initial">J</span>
        <span class="journey-intro">YOUR PERSONAL</span>
        <span class="journey-word">OURNEY</span>
      </div>
      <p class="begins-bar">BEGINS HERE</p>
    </div>
  </section>
</main>
</body>
</html>
```